Business Card Design

Looking for business card designs for a new business. there will be two cards of the same design (both lots of information below in contact info). We would like the logo diagonally across the card with the information split above and below the logo similar to sketch. happy to look at similar alternatives
Please use same colours as in logo design

Industry/Entity Type

Business

Contact Information for Business Card

Gareth Mullins
mob - 0498 172 309
ph - 02 4839 2100
fax - 02 4839 2400
email - gaz@ridgelinetrusses.com.au
14 Calloway Road, Parrinda NSW 2340

Desmond Alcott
mob - 0426 918 753
ph - 02 4839 2100
fax - 02 4839 2400
email - desmond@ridgelinetrusses.com.au

```html
<!DOCTYPE html>
<html lang="en">
<head>
<meta charset="utf-8">
<title>Ridgeline Trusses – Business Cards</title>
<link href="https://fonts.googleapis.com/css2?family=Open+Sans:wght@400;600;700&display=swap" rel="stylesheet">
<style>
  :root {
    --teal: #13847f;
    --ink: #141414;
    --paper: #ffffff;
    --backdrop: #e9e7e3;
  }
  * { box-sizing: border-box; margin: 0; padding: 0; }
  html, body { width: 768px; height: 1200px; overflow: hidden; }
  body {
    background: var(--backdrop);
    font-family: "Open Sans", Arial, sans-serif;
    position: relative;
  }
  .card { position: absolute; overflow: hidden; }

  /* Front */
  .card-front {
    left: 31px; top: 23px; width: 706px; height: 412px;
    background: var(--paper);
  }
  .card-front .diagonal { position: absolute; inset: 0; width: 100%; height: 100%; }
  .brand-front {
    position: absolute; left: 40px; top: 62px;
    display: flex; align-items: center; gap: 12px;
    color: var(--ink); font-weight: 700; font-size: 40px; letter-spacing: -0.5px;
  }
  .brand-mark { width: 26px; height: 26px; background: var(--ink); }
  .contact {
    position: absolute; right: 18px; top: 168px;
    color: var(--paper); text-align: right;
  }
  .contact-name { font-weight: 700; font-size: 20px; margin-bottom: 40px; }
  .contact-list { list-style: none; font-size: 16px; line-height: 28px; }
  .contact-list li { display: flex; justify-content: flex-end; align-items: center; gap: 6px; }
  .contact-list svg { width: 14px; height: 14px; fill: var(--paper); }
  .address {
    position: absolute; right: 18px; bottom: 20px;
    color: var(--paper); font-size: 16px;
  }

  /* Back */
  .card-back {
    left: 207px; top: 461px; width: 410px; height: 717px;
    background: var(--ink);
  }
  .website {
    position: absolute; left: 62px; top: 160px;
    writing-mode: vertical-rl;
    color: var(--paper); font-size: 20px; letter-spacing: 3.2px;
  }
  .brand-back {
    position: absolute; left: 170px; top: 92px;
    writing-mode: vertical-rl;
    display: flex; align-items: center; gap: 16px;
    color: var(--teal); font-weight: 700; font-size: 62px; line-height: 1; letter-spacing: -0.5px;
  }
  .brand-back .brand-mark { width: 40px; height: 40px; background: var(--teal); }
</style>
</head>
<body>

<section class="card card-front">
  <svg class="diagonal" viewBox="0 0 706 412" preserveAspectRatio="none" aria-hidden="true">
    <polygon points="0,402 706,22 706,412 0,412" fill="var(--teal)"/>
    <line x1="0" y1="388" x2="706" y2="6" stroke="var(--ink)" stroke-width="7"/>
  </svg>

  <div class="brand-front"><span class="brand-mark"></span>Ridgeline Trusses</div>

  <div class="contact">
    <p class="contact-name">Desmond Alcott</p>
    <ul class="contact-list">
      <li><svg viewBox="0 0 16 16"><path d="M3 1l3 0 1 4-2 1a9 9 0 005 5l1-2 4 1 0 3c0 1-1 2-2 2A13 13 0 011 3c0-1 1-2 2-2z"/></svg>02 4839 2100</li>
      <li><svg viewBox="0 0 16 16"><path d="M4 0h8a1 1 0 011 1v14a1 1 0 01-1 1H4a1 1 0 01-1-1V1a1 1 0 011-1zm1 2v9h6V2z"/></svg>0426 918 753</li>
      <li><svg viewBox="0 0 16 16"><path d="M4 1h8v4H4zM1 6h14v7h-2v-3H3v3H1zM4 11h8v4H4z"/></svg>02 4839 2400</li>
      <li><svg viewBox="0 0 16 16"><path d="M1 3h14v10H1zm1 1l6 5 6-5z"/></svg>desmond@ridgelinetrusses.com.au</li>
    </ul>
  </div>

  <p class="address">14 Calloway Road, Parrinda NSW 2340</p>
</section>

<section class="card card-back">
  <p class="website">www.ridgelinetrusses.com.au</p>
  <div class="brand-back"><span class="brand-mark"></span>Ridgeline Trusses</div>
</section>

</body>
</html>
```